Webdesign für Sexualpädagogik
Zielgruppe
- Sexualpädagogik, Beratung und Sexualtherapie
- Vorträge und Seminare für Unternehmen / Institutionen Vorträge Sexualität in der Pflege / im Alter / Grenzen wahrnehmen
- Wechseljahreberatung, Beratung in der Lebensmitte
- ZIelgruppe: Menschen, die sich weiternetwickeln möchten, die Problme mit ihrer Sexualität haben, Paare, Jugendliche
letztes Interview in der Zeitung: https://www.talbote-beispiel.ch/talbote/zeitung/frontal-interview/sexualitaet-hoert-nicht-beim-eintritt-ins-spital-auf/
Aufgabenstellung
- bestehende Internetseite siehe unten: Schrift ist Especial Key von Wolkenweg
- auf dem Briefpapier bisher noch der Fachbuchhandel und Onlinhandel, aber beides nicht mehr
- Bilder zum Thema bereist vorhanden
- für Werbeflyer habe ich die Therapie in dunkelblau gehalten udn in der sexualpädagogik in hellblau
der kramhaus wird aus der website entfernet

```html
<!DOCTYPE html>
<html lang="de">
<head>
<meta charset="utf-8">
<title>Wolkenweg – Sexualpädagogik</title>
<link rel="stylesheet" href="https://fonts.googleapis.com/css2?family=Roboto:ital,wght@0,300;0,400;0,500;0,700;1,400;1,500&family=Montserrat:wght@500&display=swap">
<style>
:root{
  --brand:#0a4ba8;
  --brand-dark:#1f2a8a;
  --ink:#222;
  --muted:#666;
  --panel:#f4f4f4;
  --line:#e2e2e2;
  --accent:#f5c242;
  --hero-label:#333;
}
*{margin:0;padding:0;box-sizing:border-box}
html,body{width:1091px;height:1200px;overflow:hidden;background:#fff}
body{position:relative;font-family:"Roboto",sans-serif;color:var(--ink)}
.side-rail{position:absolute;left:0;top:0;width:61px;height:1200px;background:var(--brand)}
.side-rail__name{position:absolute;left:31px;top:220px;transform:translate(-50%,-50%) rotate(-90deg);color:#fff;font-size:22px;font-weight:500;letter-spacing:2px;white-space:nowrap}
.masthead{position:absolute;left:300px;top:18px;width:520px;text-align:center}
.masthead__mark{position:absolute;left:12px;top:4px;width:64px;height:64px;border-radius:50%;background:var(--brand)}
.masthead__name{font-size:42px;font-weight:500;color:var(--brand);line-height:48px;margin-left:80px}
.masthead__tag{margin-left:80px;font-style:italic;font-weight:500;font-size:12px;line-height:20px}
.masthead__tag em{color:var(--brand-dark)}
.nav{position:absolute;left:136px;top:134px;width:818px;height:41px;background:var(--brand);display:flex;justify-content:center;gap:64px;align-items:center}
.nav a{color:#fff;text-decoration:none;font-weight:500;font-size:12px}
.hero{position:absolute;left:137px;top:175px;width:817px;height:192px;background:linear-gradient(180deg,#eef0f3 0%,#d9d2cc 55%,#b65a36 78%,#8a3c22 100%)}
.hero__label{position:absolute;left:0;top:65px;height:52px;padding:0 24px 0 10px;background:var(--hero-label);color:#fff;font-weight:300;font-size:31px;line-height:52px;border-right:6px solid var(--accent)}
.intro{position:absolute;left:137px;top:402px;width:476px;font-weight:300;font-size:12.3px;line-height:20.5px;text-align:justify}
.intro p{padding-left:22px}
.intro p:first-child{border-left:4px solid var(--brand);padding-left:18px;margin-bottom:20px}
.intro-photo{position:absolute;left:638px;top:404px;width:317px;height:183px;background:linear-gradient(160deg,#5a5e5c,#3a3d3c)}
.goals{position:absolute;left:137px;top:626px;width:817px;height:39px;background:var(--brand);color:#fff;text-align:center;font-size:17px;font-weight:500;line-height:39px}
.goals::after{content:"";position:absolute;left:11px;bottom:-8px;border:8px solid transparent;border-top-color:var(--brand);border-bottom:0}
.checklist{position:absolute;list-style:none;font-weight:300;font-size:12.3px;line-height:20.5px}
.checklist li{position:relative;padding-left:28px;margin-bottom:7px}
.checklist svg{position:absolute;left:2px;top:4px;width:14px;height:14px}
.checklist--left{left:147px;top:696px;width:400px}
.checklist--right{left:568px;top:682px;width:385px}
.testimonial{position:absolute;left:137px;top:874px;width:816px;height:224px;background:var(--panel);border:1px solid var(--line)}
.testimonial__photo{position:absolute;left:82px;top:46px;width:130px;height:136px;border-radius:50%;background:radial-gradient(circle at 50% 45%,#e8cdb6,#b89070 70%,#8d6a50)}
.testimonial__quote{position:absolute;left:200px;top:36px;font-size:80px;font-weight:700;color:var(--brand);line-height:80px}
.testimonial__stars{position:absolute;left:267px;top:43px;display:flex;gap:5px}
.testimonial__name{position:absolute;left:267px;top:67px;font-family:"Montserrat",sans-serif;font-weight:500;font-size:12px;letter-spacing:2.5px;color:var(--muted)}
.testimonial__text{position:absolute;left:267px;top:90px;width:500px;font-size:10.8px;line-height:15.8px;color:var(--muted)}
.testimonial__rule{position:absolute;left:267px;top:171px;width:21px;height:3px;background:var(--brand)}
.testimonial__arrow{position:absolute;top:109px;width:12px;height:14px}
.footer{position:absolute;left:134px;top:1098px;width:820px;height:48px;background:var(--brand);display:flex;align-items:center;padding:0 17px;font-size:11px;color:#fff}
.footer a{color:#fff;text-decoration:none;margin-right:22px}
.footer .footer__legal{margin-left:auto;margin-right:0;font-weight:500}
.social{position:absolute;right:148px;top:1167px;display:flex;gap:14px;font-size:10px;color:var(--brand)}
.social span{display:flex;align-items:center;gap:4px}
.social i{width:10px;height:10px;border-radius:50%;background:var(--brand);display:inline-block}
</style>
</head>
<body>
<aside class="side-rail"><div class="side-rail__name">Wolkenweg</div></aside>

<header class="masthead">
  <div class="masthead__mark"></div>
  <div class="masthead__name">Wolkenweg</div>
  <div class="masthead__tag">Fachstelle Fur <em>Sexualpadagogik, Beratung</em> und <em>Therapie</em><br>Mara Feldkirch</div>
</header>

<nav class="nav">
  <a href="#">HOME</a><a href="#">ÜBER MICH</a><a href="#">GÄSTEBUCH</a><a href="#">NEWSLETTER</a><a href="#">PREISE</a><a href="#">KONTAKT</a>
</nav>

<section class="hero" role="img" aria-label="Foto: Jugendliche im Klassenzimmer mit einer anatomischen Schautafel">
  <h1 class="hero__label">Sexualpädagogik</h1>
</section>

<div class="intro">
  <p>Sexualpädagogik ist die pädagogische Arbeit mit Mädchen und Jungen zu deren Fragestellungen zu Liebe, Gefühlen und Sexualität sowie zu Gender Aspekten. Ziel ist es, durch Information, Aufklärung, Beratung und Begleitung die Verantwortungsbereitschaft des / der Einzelnen zu unterstützen.</p>
  <p>Ziel ist es auch, verantwortliches Handeln gegenüber sich selbst und anderen zu fördern und bewusst zu erleben. Ziel ist es, Themen der Sexualität auf der Basis von Gesundheit und Lebensfreude zu vermitteln. Im Zentrum stehen die sexuelle Gleichwertigkeit von Mann und Frau, sowie die Unterschiede der Geschlechter.</p>
</div>
<div class="intro-photo" role="img" aria-label="Foto: zwei Jugendliche vor einer Tafel voller Fragezeichen"></div>

<h2 class="goals">Ziel ist es, Wissen und Anregungen zu vermitteln über :</h2>

<ul class="checklist checklist--left">
  <li><svg viewBox="0 0 14 14"><path d="M1 7l4 5 8-11" fill="none" stroke="#0a4ba8" stroke-width="2"/></svg>Wissen über den weiblichen und männlichen Körper</li>
  <li><svg viewBox="0 0 14 14"><path d="M1 7l4 5 8-11" fill="none" stroke="#0a4ba8" stroke-width="2"/></svg>Wissen über weibliche und männliche Sexualitäten</li>
  <li><svg viewBox="0 0 14 14"><path d="M1 7l4 5 8-11" fill="none" stroke="#0a4ba8" stroke-width="2"/></svg>Fertigkeiten zur Entwicklung der eigenen Sexualität<br>Sexuelle Selbstsicherheit im Zeitalter der Entschubladisierung von Hetero-, Homo-,&nbsp;&nbsp; Mono-, Bi-, Metro-, Trans- und Pädosexualität</li>
</ul>
<ul class="checklist checklist--right">
  <li><svg viewBox="0 0 14 14"><path d="M1 7l4 5 8-11" fill="none" stroke="#0a4ba8" stroke-width="2"/></svg>Sexuelles Begehren im Dschungel alltäglicher Attraktionen - Intimität und Öffentlichkeit</li>
  <li><svg viewBox="0 0 14 14"><path d="M1 7l4 5 8-11" fill="none" stroke="#0a4ba8" stroke-width="2"/></svg>Kompetenzen über und mit Sexualität zu kommunizieren</li>
  <li><svg viewBox="0 0 14 14"><path d="M1 7l4 5 8-11" fill="none" stroke="#0a4ba8" stroke-width="2"/></svg>Medizinische und juristische Kenntnisse</li>
</ul>

<section class="testimonial">
  <svg class="testimonial__arrow" style="left:26px" viewBox="0 0 12 14"><path d="M9 1L3 7l6 6" fill="none" stroke="#222" stroke-width="2"/></svg>
  <div class="testimonial__photo" role="img" aria-label="Porträtfoto der Kundin"></div>
  <div class="testimonial__quote">“</div>
  <div class="testimonial__stars">
    <svg width="11" height="11" viewBox="0 0 10 10"><path d="M5 0l1.5 3.3 3.5.3-2.7 2.3.9 3.5L5 7.5 1.8 9.4l.9-3.5L0 3.6l3.5-.3z" fill="#0a4ba8"/></svg>
    <svg width="11" height="11" viewBox="0 0 10 10"><path d="M5 0l1.5 3.3 3.5.3-2.7 2.3.9 3.5L5 7.5 1.8 9.4l.9-3.5L0 3.6l3.5-.3z" fill="#0a4ba8"/></svg>
    <svg width="11" height="11" viewBox="0 0 10 10"><path d="M5 0l1.5 3.3 3.5.3-2.7 2.3.9 3.5L5 7.5 1.8 9.4l.9-3.5L0 3.6l3.5-.3z" fill="#0a4ba8"/></svg>
    <svg width="11" height="11" viewBox="0 0 10 10"><path d="M5 0l1.5 3.3 3.5.3-2.7 2.3.9 3.5L5 7.5 1.8 9.4l.9-3.5L0 3.6l3.5-.3z" fill="#0a4ba8"/></svg>
    <svg width="11" height="11" viewBox="0 0 10 10"><path d="M5 0l1.5 3.3 3.5.3-2.7 2.3.9 3.5L5 7.5 1.8 9.4l.9-3.5L0 3.6l3.5-.3z" fill="#0a4ba8"/></svg>
  </div>
  <div class="testimonial__name">JONAS BERGLIND</div>
  <p class="testimonial__text">Lorem ipsum dolor sit amet, consectetuer adipiscing elit. Class aptent taciti sociosqu ad litora torquent per conubia nostra, per inceptos hymenaeos. Nulla non arcu lacinia neque faucibus fringilla. Ut enim ad minim veniam, quis nostrud exercitation ullamco laboris nisi ut aliquip ex ea commodo consequat. Nam quis nulla. Ut tempus purus at lorem.</p>
  <div class="testimonial__rule"></div>
  <svg class="testimonial__arrow" style="left:776px" viewBox="0 0 12 14"><path d="M3 1l6 6-6 6" fill="none" stroke="#222" stroke-width="2"/></svg>
</section>

<footer class="footer">
  <a href="#">Impressum</a><a href="#">Lageplan</a><a href="#">News</a><a href="#">Nächste Seminare</a><a href="#">Kontakt</a><a href="#">über Mara Feldkirch / Wolkenweg</a>
  <a class="footer__legal" href="#">Datenschutz | Terms &amp; Bedingungen</a>
</footer>

<div class="social"><span><i></i>Kontaktnetz</span><span><i></i>Freundesbuch</span></div>
</body>
</html>
```